Harbinger and Lantern Website

We are a private investigation that people turn to when they seek answers. We provide all types of investigation services as well as security and debt collection but mainly we specialise in digital forensic investigation. This site will be the first representation that potential clients see. We need a site that can work on all browsers so not too many animations. The theme we are going for is "Pallor" the TV show but keeping the law enforcement look. We want it to expand on the logo of our company that is strength and pride (refer to files attached). The logo and mission statement must stand out.
The relevant info is attached in .doc documents
Updates

Hi,

I have uploaded a slightly different version of the logo and I do prefer the new version and made a FEW but important updates and additions to the website info. Sorry for the inconvenience.

Hi, 

Sorry just one last thing can you please put the following on the website 'Harbinger and Lantern is a South Australian owned business and we service all of Australia.' 

I have increased the budget.

Hi,

I've increased the budget slightly. I will continue to increase it as long as the quality of designs match it.

I have increased the budget. I will increase it more if I see some designs that warrant the increase.

I have extended the deadline by 3 days.

Hi,

Forget the brief and please take a look at this link and that is the type of design I want. I want people to look at it and think modern, professional, digital, forensic investigation. I have not seen anything that makes me think "wow" so please submit some new designs. I will increase the budget when I start to see designs that I like. 

regarding the last message, this is the link

https://www.vantorel-example.org

Reason: Have not seen anything that stands out from the rest.

Reason: To let designers finish off their current concepts that they may be working on.

Target Market(s)

Average to corporate people seeking professionalism and a firm that can supply answers that traditional law enforcement agencies fail to provide

Industry/Entity Type

Security

Requirements
Must have
• A professional QRD, Southern Tablelands Constabulary website look mixed with a theme from the TV show "Pallor" and the ability to download the business cards (refer to attached files)
Should not have
• cartoon images and anything relating to Ambrose Pettigrew

```html
<!DOCTYPE html>
<html lang="en">
<head>
<meta charset="utf-8">
<title>Harbinger &amp; Lantern — Private Intelligence &amp; Investigation Group</title>
<link rel="stylesheet" href="https://fonts.googleapis.com/css2?family=Arimo:ital,wght@0,400;0,700;1,400&display=swap">
<style>
:root{
  --gold:#a88b25;
  --gold-light:#c9a93a;
  --gold-btn-top:#e4cf7c;
  --gold-btn-bot:#bfa042;
  --ink:#1a1a1a;
  --text:#333;
  --nav-bg:#0c0c0c;
  --footer-bg:#232323;
  --footer-text:#9a9a9a;
  --bottom-bg:#141414;
  --line:#e4e4e4;
}
*{box-sizing:border-box;margin:0;padding:0}
html,body{width:1169px;height:1200px;overflow:hidden}
body{font-family:"Arimo",Arial,sans-serif;background:#fff;color:var(--text);position:relative}
.wrap{position:absolute;left:0;top:0;width:1169px;height:1200px}
/* header */
.top{position:absolute;left:0;top:0;width:1169px;height:97px;background:linear-gradient(#fff,#ececec)}
.brand{position:absolute;left:118px;top:18px;display:flex;align-items:center;gap:10px;z-index:5}
.brand-mark{width:74px;height:74px;border-radius:50%;background:var(--gold);flex:none}
.brand-name{font-size:15px;font-weight:700;color:var(--ink);line-height:1.2;width:100px}
.phone{position:absolute;right:104px;top:22px;display:flex;gap:10px;align-items:center}
.phone-num{font-size:19px;font-weight:700;color:#444;line-height:1}
.phone-hours{font-size:10px;color:#999;margin-top:2px}
.mails{position:absolute;right:104px;top:70px;font-size:12px;color:#333}
.mails span+span{border-left:1px solid #ccc;margin-left:6px;padding-left:8px}
/* nav */
.nav{position:absolute;left:0;top:97px;width:1169px;height:41px;background:linear-gradient(#1e1e1e,#000)}
.nav ul{list-style:none;position:absolute;left:306px;top:13px;display:flex;font-size:14px;color:#fff}
.nav li.active{color:var(--gold-light)}
/* hero */
.hero{position:absolute;left:0;top:138px;width:1169px;height:290px;background:radial-gradient(ellipse at 60% 40%,#353535,#1f1f1f)}
.hero h1{position:absolute;left:180px;top:62px;font-size:24px;color:#fff;font-weight:700;letter-spacing:-.6px}
.hero h2{position:absolute;left:180px;top:98px;font-size:15px;color:var(--gold);font-weight:700;letter-spacing:-.3px}
.hero p{position:absolute;left:180px;top:127px;width:380px;font-size:14px;line-height:17px;color:#bbb}
.btn-dark{position:absolute;left:180px;top:207px;width:108px;height:30px;border-radius:3px;background:linear-gradient(#3a3a3a,#141414);color:var(--gold-light);font-size:14px;text-align:center;line-height:30px;box-shadow:0 2px 4px rgba(0,0,0,.6)}
.dots{position:absolute;left:309px;top:255px;display:flex;gap:18px}
.dots i{width:12px;height:12px;border-radius:50%;background:#111}
.dots i:first-child{background:var(--gold)}
.arrow{position:absolute;width:42px;height:36px;background:#0f0f0f}
.arrow.left{left:112px;top:118px}.arrow.right{left:1024px;top:115px}
.hero-visual{position:absolute;left:614px;top:205px;width:402px;height:297px;z-index:4;border-radius:6px;background:radial-gradient(ellipse at 55% 40%,#c2a548,#7d6618 55%,#1a1a1a)}
/* news */
.news{position:absolute;left:0;top:428px;width:1169px;height:58px;background:linear-gradient(#b39a33,#8d7418)}
.news b{position:absolute;left:112px;top:22px;font-size:16px;color:#222}
.news em{position:absolute;left:172px;top:24px;font-size:13px;color:#f1e6c0}
/* features */
.features{position:absolute;left:0;top:486px;width:1169px;height:220px;background:linear-gradient(#ececec,#fff 40%)}
.feature{position:absolute;top:42px;width:272px}
.feature h3{font-size:15px;font-weight:700;color:var(--ink);margin-bottom:7px;letter-spacing:-.2px}
.feature p{font-size:12.5px;line-height:15.5px;color:#333;padding-left:1px}
.feature .btn{display:inline-block;margin-top:11px;padding:0 12px;height:22px;line-height:22px;font-size:12px;border-radius:3px}
.btn.black{background:#111;color:var(--gold-light)}
.btn.gold{background:linear-gradient(var(--gold-btn-top),var(--gold-btn-bot));color:#222}
.f1{left:112px}.f2{left:445px}.f3{left:803px}
.sep{position:absolute;top:40px;width:1px;height:150px;background:linear-gradient(#fff,#ddd,#fff);box-shadow:4px 0 8px rgba(0,0,0,.06)}
.rule{position:absolute;left:112px;top:713px;width:954px;height:1px;background:var(--line)}
/* testimonials */
.section-title{position:absolute;font-size:15px;font-weight:700;color:var(--ink);letter-spacing:-.3px}
.quote-mark{position:absolute;left:114px;top:776px;font-size:40px;color:#bbb;font-family:Georgia,serif;line-height:1}
.quote{position:absolute;left:151px;top:778px;width:440px;font-size:12.5px;line-height:15.5px;font-style:italic;color:#555}
.cite{position:absolute;left:151px;top:852px;font-size:13px;color:var(--gold)}
.card-box{position:absolute;left:637px;top:779px;width:429px;height:107px;background:#e6e6e6;border-radius:3px}
.avatar{position:absolute;left:25px;top:18px;width:76px;height:76px;border-radius:50%;background:radial-gradient(#fafafa,#c9c9c9);box-shadow:0 0 0 2px #d4d4d4}
.dl-btn{position:absolute;left:147px;top:21px;width:225px;height:44px;border-radius:3px;background:linear-gradient(#2f2f2f,#050505);color:var(--gold-light);font-size:18px;font-weight:700;letter-spacing:1px;text-align:center;line-height:44px}
.dl-meta{position:absolute;left:128px;top:81px;font-size:12px;color:#555}
.dl-meta b{color:#333}
/* footer */
.footer{position:absolute;left:0;top:927px;width:1169px;height:231px;background:var(--footer-bg)}
.fcol{position:absolute;top:33px}
.fcol h4{font-size:16px;color:var(--gold);font-weight:700;margin-bottom:13px}
.fcol ul{list-style:none;font-size:12.5px;color:var(--footer-text)}
.fcol li{height:23.4px;padding-left:11px;position:relative}
.fcol li::before{content:"";position:absolute;left:0;top:5px;border-left:4px solid #888;border-top:3px solid transparent;border-bottom:3px solid transparent}
.fcol li.current{color:#fff}
.c1{left:112px}.c2{left:306px}.c3{left:481px}
.fcontact{position:absolute;left:680px;top:40px;width:330px;text-align:center;color:#bbb;font-size:12.5px;line-height:15px}
.fcontact .name{font-size:18px;color:#fff;line-height:22px}
.fcontact .tag{font-size:13.5px;color:#7a6a2a}
.fphone{display:flex;justify-content:center;align-items:center;gap:10px;margin-top:12px;font-size:18px;color:#fff}
.bottom{position:absolute;left:0;top:1158px;width:1169px;height:42px;background:var(--bottom-bg);text-align:center;font-size:12px;color:#555;line-height:42px}
</style>
</head>
<body>
<div class="wrap">
  <header class="top">
    <div class="phone">
      <svg width="34" height="24" viewBox="0 0 34 24" aria-hidden="true"><path d="M2 9C6 2 28 2 32 9l-4 4-5-3V7H11v3l-5 3z" fill="#c2a548"/><rect x="8" y="13" width="18" height="10" rx="2" fill="#c2a548"/><circle cx="17" cy="18" r="3" fill="#fff"/></svg>
      <div><div class="phone-num">0400 555 218</div><div class="phone-hours">Contact Hours: 24hours</div></div>
    </div>
    <div class="mails"><span>ben@harbingerlantern.example</span><span>managers@harbingerlantern.example</span></div>
  </header>
  <div class="brand"><span class="brand-mark"></span><span class="brand-name">Harbinger &amp; Lantern</span></div>
  <nav class="nav">
    <ul>
      <li style="width:80px">Home</li><li style="width:87px">About</li><li class="active" style="width:98px">Science</li><li style="width:145px">Unsolved Cases</li><li style="width:150px">Bullying/Stalking</li><li style="width:143px">Missing Persons</li><li>Contact</li>
    </ul>
  </nav>
  <section class="hero">
    <div class="arrow left"><svg width="42" height="36"><path d="M25 8 17 18l8 10" stroke="#ddd" stroke-width="1.5" fill="none"/></svg></div>
    <div class="arrow right"><svg width="42" height="36"><path d="M17 8l8 10-8 10" stroke="#c9a93a" stroke-width="1.5" fill="none"/></svg></div>
    <h1>Welcome to Harbinger &amp; Lantern</h1>
    <h2>Private Intelligence &amp; Investigation Group</h2>
    <p>Through integrity and professionalism we will use our experience and resources as well as thinking outside the box to deliver results and services that exceed our clients’ expectations.</p>
    <div class="btn-dark">Read more</div>
    <div class="dots"><i></i><i></i><i></i></div>
  </section>
  <div class="hero-visual" role="img" aria-label="Computer monitor showing the company emblem on a gold screen"></div>
  <div class="news"><b>NEWS</b><em>Lorem ipsum dolor sit amet, consectetuer adipiscing elit, sed diam...</em></div>
  <section class="features">
    <article class="feature f1"><h3>ADVANTAGE</h3><p>What makes Harbinger and Lantern stand out from the rest is we believe investigation is not just a service, it is a science and we are the scientists of investigation.</p><span class="btn black">Read more</span></article>
    <div class="sep" style="left:408px"></div>
    <article class="feature f2"><h3>INTRO</h3><p>Harbinger is a private investigation and intelligence group and an alternative to law enforcement agencies. We conduct all types of investigations including factual, forensic and surveillance.</p><span class="btn gold">Read more</span></article>
    <div class="sep" style="left:761px"></div>
    <article class="feature f3"><h3>QUALIFICATION</h3><p>All our investigators come from successful careers in various fields vital to investigation. We only employ the best of the best to guarantee you the client results that [..]</p><span class="btn gold">Read more</span></article>
  </section>
  <div class="rule"></div>
  <h3 class="section-title" style="left:112px;top:742px">CLIENT TESTIMONIALS</h3>
  <div class="quote-mark">“</div>
  <p class="quote">Lorem ipsum dolor sit amet, consectetuer adipiscing elit, sed diam nonummy nibh euismod tincidunt ut laoreet dolore magna aliquam erat volutpat. Ut wisi enim ad minim veniam, quis nostrud exerci tation ullamcorper suscipit lobortis nisl ut aliquip ex ea commodo consequat.</p>
  <div class="cite">Tom’s - Marlowfield, SA</div>
  <h3 class="section-title" style="left:637px;top:744px">BUSINESS CARD DOWNLOADS</h3>
  <div class="card-box">
    <div class="avatar" role="img" aria-label="Business card holder icon"></div>
    <div class="dl-btn">DOWNLOADS</div>
    <div class="dl-meta"><b>Size</b> 593kb &nbsp;&nbsp; <b>Type</b> Portable Document Format (PDF)</div>
  </div>
  <footer class="footer">
    <div class="fcol c1"><h4>MENU</h4><ul><li>About</li><li>Science</li><li class="current">Unsolved Cases</li><li>Bullying/Stalking</li><li>Missing Persons</li><li>Contact</li></ul></div>
    <div class="fcol c2"><h4>LINKS</h4><ul><li>Links 1</li><li>Links 2</li><li>Links 3</li><li>Links 4</li><li>Links 5</li><li>Links 6</li></ul></div>
    <div class="fcol c3"><h4>FOLLOW US</h4><ul><li>Friendwall</li><li>Chirper</li><li>ProNet</li><li>Goldlist</li></ul></div>
    <div class="fcontact">
      <div class="name">Harbinger &amp; Lantern</div>
      <div class="tag">Private Intelligence, Investigation &amp; Security Group.</div>
      <div>Investigators - Marlowfield, SA</div>
      <div style="margin-top:17px">ben@harbingerlantern.example<br>managers@harbingerlantern.example</div>
      <div class="fphone"><svg width="18" height="14" viewBox="0 0 34 24" aria-hidden="true"><path d="M2 9C6 2 28 2 32 9l-4 4-5-3V7H11v3l-5 3z" fill="#c2a548"/><rect x="8" y="13" width="18" height="10" rx="2" fill="#c2a548"/></svg>0400 555 218</div>
    </div>
  </footer>
  <div class="bottom">Copyright © 2012 Harbinger &amp; Lantern. All right reserved</div>
</div>
</body>
</html>
```